WebHaven Sentry (Parental Guidance software) brochure

We want a brochure that gives an overview of the service that we provide which can be emailled to users at their request. Including the front cover it should be 4-5 pages in length. The website https://www.webhavensentry.co.uk describes our service.
The industry terms our app Parental Control but we call it Parental Guidance so we don't want the term Parental Control on here.

We can provide the text that can go into the brochure. The design should be informal but informative. We are also a member of the NCB and DSR so we need to include logos in the brochure somewhere.

Target Market(s)

The target market is parents who are visiting the website, this will be a downloadable brochure.

Industry/Entity Type

Information Technology

Requirements
Must have
• The front of the brochure should be a cover page with images and the words "Parental Guidance with WebHaven Sentry"
• The second page should have some text about the service and a small piece about the company behind it, Marlow IT Ltd and some of the main features of the service i.e. what it can do including some screenshots.
• The third page would have statistics such as
• Page 3
• Statistics page –
• 1 in 3 Internet users are children.
• 1 in 5 eight to eleven-year olds have a social media profile.
• 1 in 3 children have been a victim of cyberbullying.
• By 15 years old 65% of children have seen online pornography. Children were most likely to see it via pop-ups than by searching for it.
• Just over half of boys (53%) who had seen pornography thought it was ‘realistic’.
• One in three parents (33%) claims to filter their child’s internet use and one in four (27%) uses monitoring software.
• Overall, only a quarter of children (27%) and a third of parents think parents are effective in helping to keep children safe online.
• The fourth page would give details of facebook and twitter pages, what support we provide (currently email based), as details of future features.
Should not have
• Images from the website...The brochure should be individual to the website as people will be requesting it from the website.
• Should not have the term Parental Control, but can use Parental Guidance

```html
<!DOCTYPE html>
<html lang="en">
<head>
<meta charset="utf-8">
<title>WebHaven Sentry – Features and Statistics</title>
<link rel="stylesheet" href="https://fonts.googleapis.com/css2?family=Montserrat:wght@600;700;800&family=Open+Sans:wght@400;600&display=swap">
<style>
  :root {
    --backdrop: #d8cfca;
    --paper: #ffffff;
    --navy: #0d3a5c;
    --sky: #1f80ad;
    --band: #d3e2ee;
    --ring: #dcdcdc;
    --ink: #1b1b1b;
    --badge: #111111;
  }
  * { box-sizing: border-box; margin: 0; padding: 0; }
  html, body { width: 1200px; height: 833px; overflow: hidden; }
  body { background: var(--backdrop); font-family: "Open Sans", Arial, sans-serif; color: var(--ink); }

  .spread { position: absolute; left: 20px; top: 20px; width: 1160px; height: 793px; display: flex; box-shadow: 0 6px 20px rgba(0,0,0,.15); }
  .page { position: relative; width: 580px; height: 793px; background: var(--paper); overflow: hidden; }
  .page--features { border-right: 1px solid #e5e5e5; display: flex; flex-direction: column; }

  /* Features page */
  .feature { position: relative; flex: 1 1 auto; padding: 14px 30px 10px 30px; display: grid; grid-template-columns: 56px 1fr 76px; column-gap: 16px; align-content: start; }
  .feature--band { background: linear-gradient(90deg, var(--band) 0%, #e7eff6 60%, #ffffff 100%); }
  .feature__title { grid-column: 1 / 4; justify-self: start; font-family: "Montserrat", Arial, sans-serif; font-weight: 700; font-size: 15px; color: var(--navy); border-bottom: 1.5px solid var(--sky); padding-bottom: 3px; margin-bottom: 8px; }
  .feature__text { grid-column: 2; font-size: 11px; line-height: 1.4; }
  .feature__icon { width: 52px; height: 44px; background: var(--navy); border-radius: 4px; opacity: .85; }
  .feature__deco { width: 74px; height: 50px; background: linear-gradient(135deg, var(--sky), #7fb5d2); border-radius: 6px; }

  .stores { display: flex; gap: 26px; margin-top: 10px; grid-column: 1 / 4; }
  .store { display: flex; flex-direction: column; gap: 3px; font-size: 10px; }
  .store__badge { width: 150px; height: 40px; background: var(--badge); border-radius: 6px; color: #fff; font-family: "Open Sans", Arial, sans-serif; font-weight: 600; font-size: 15px; display: flex; align-items: center; justify-content: center; }

  /* Statistics page */
  .stats__title { position: absolute; top: 30px; left: 0; width: 100%; text-align: center; font-family: "Montserrat", Arial, sans-serif; font-weight: 800; font-size: 30px; color: var(--ink); }
  .stats__rule { position: absolute; top: 76px; left: 160px; width: 260px; height: 2px; background: var(--sky); }
  .people { position: absolute; display: flex; flex-direction: column; align-items: center; }
  .people__row { display: flex; gap: 8px; }
  .person { width: 40px; height: 66px; border-radius: 20px 20px 6px 6px; background: var(--navy); }
  .person--highlight { background: var(--sky); }
  .people__caption { font-size: 10.5px; text-align: center; border-top: 1.5px solid var(--sky); padding-top: 3px; margin-top: 4px; }

  .donut { position: absolute; display: flex; flex-direction: column; align-items: center; text-align: center; }
  .donut__label { font-family: "Montserrat", Arial, sans-serif; font-weight: 700; font-size: 14px; fill: var(--navy); }
  .donut__caption { font-size: 10.5px; line-height: 1.3; margin-top: 6px; width: 250px; }

  .bars { position: absolute; display: flex; flex-direction: column; align-items: center; text-align: center; }
  .bars__chart { display: flex; align-items: flex-end; gap: 18px; height: 130px; }
  .bar { width: 62px; display: flex; flex-direction: column; align-items: center; }
  .bar__value { font-family: "Montserrat", Arial, sans-serif; font-weight: 700; font-size: 15px; }
  .bar__fill { width: 62px; display: flex; align-items: flex-end; justify-content: center; color: #fff; font-size: 9px; padding-bottom: 3px; }
  .bar--parents .bar__value { color: var(--navy); }
  .bar--parents .bar__fill { background: var(--navy); height: 100px; }
  .bar--child .bar__value { color: var(--sky); }
  .bar--child .bar__fill { background: var(--sky); height: 82px; }
  .bars__caption { font-size: 10.5px; line-height: 1.3; margin-top: 6px; width: 260px; }
  .stats__foot { position: absolute; top: 760px; left: 150px; width: 280px; height: 1.5px; background: var(--sky); }
</style>
</head>
<body>
<div class="spread">

  <section class="page page--features">
    <article class="feature feature--band">
      <h2 class="feature__title">Dashboard to monitor usage</h2>
      <div class="feature__icon" role="img" aria-label="Monitor showing a usage chart icon"></div>
      <p class="feature__text">Shows the top 10 sites visited, amount of time spent on those sites, top 10 sites blocked sites, amount of bandwidth consumed and can be filtered per user basis for the last day, week and month.</p>
    </article>
    <article class="feature">
      <h2 class="feature__title">Limit Device Bandwidth Utilisation</h2>
      <div></div>
      <p class="feature__text">The amount of bandwidth (i.e. the amount of data that the device downloads) can be limited. This is particularly useful for households who pay for a set amount of data usage a month.</p>
      <div class="feature__deco" role="img" aria-label="Outline drawing of a desktop, tablet and phone"></div>
    </article>
    <article class="feature feature--band">
      <h2 class="feature__title">Device Access Times</h2>
      <div class="feature__icon" role="img" aria-label="Calendar icon"></div>
      <p class="feature__text">The device can be set so that it can only connect to the Internet for certain periods of the day such as between 4PM and 7PM. Limitations can be set so that the device can only access the internet for a certain period of time in 24 hours, such as 2 hours of usage every 24 hours.</p>
    </article>
    <article class="feature">
      <h2 class="feature__title">Block Inappropriate Content</h2>
      <div></div>
      <p class="feature__text">Restrictions can be placed onto the device so that users cannot visit sites deemed inappropriate including phishing sites which is a site that purports to be a well known site (commonly a financial institution) in order to trick you into entering in your login details in order to gain access to those services.</p>
      <div class="feature__deco" role="img" aria-label="Shield with padlock illustration"></div>
    </article>
    <article class="feature feature--band">
      <h2 class="feature__title">See what websites have been visited</h2>
      <div class="feature__icon" role="img" aria-label="Presenter at a chart board illustration"></div>
      <p class="feature__text">You are able to see reports on which websites have been visited and how long has been spent on these websites.</p>
    </article>
    <article class="feature">
      <h2 class="feature__title">Supports Multiple Devices</h2>
      <div></div>
      <p class="feature__text">Supported on PaneOS, Droidix, OrbitOS and Emberread devices.</p>
      <div class="feature__deco" role="img" aria-label="Supported device platform symbols"></div>
      <div class="stores">
        <div class="store"><span>Get it for OrbitOS</span><span class="store__badge">App Market</span></div>
        <div class="store"><span>Get it for Droidix</span><span class="store__badge">Play Bazaar</span></div>
      </div>
    </article>
  </section>

  <section class="page page--stats">
    <h1 class="stats__title">Statistics Page</h1>
    <div class="stats__rule"></div>

    <div class="people" style="left:40px; top:130px;">
      <div class="people__row" role="img" aria-label="Three child figures, one highlighted">
        <span class="person person--highlight"></span><span class="person"></span><span class="person"></span>
      </div>
      <p class="people__caption">1 in 3 Internet users are children.</p>
    </div>

    <div class="people" style="left:350px; top:100px;">
      <div class="people__row" role="img" aria-label="Three child figures, one highlighted">
        <span class="person person--highlight"></span><span class="person"></span><span class="person"></span>
      </div>
      <p class="people__caption">1 in 3 children have been a victim<br>of cyberbullying.</p>
    </div>

    <div class="people" style="left:150px; top:230px;">
      <div class="people__row" role="img" aria-label="Five child figures, one highlighted">
        <span class="person person--highlight"></span><span class="person"></span><span class="person"></span><span class="person"></span><span class="person"></span>
      </div>
      <p class="people__caption">1 in 5 eight to eleven-year olds have a social media profile.</p>
    </div>

    <figure class="donut" style="left:30px; top:360px;">
      <svg width="110" height="110" viewBox="0 0 110 110" role="img" aria-label="65 percent donut chart">
        <circle cx="55" cy="55" r="40" fill="none" stroke="var(--ring)" stroke-width="18"/>
        <circle cx="55" cy="55" r="40" fill="none" stroke="var(--navy)" stroke-width="18" stroke-dasharray="163.4 251.3" transform="rotate(-90 55 55)"/>
        <text x="55" y="60" text-anchor="middle" class="donut__label">65%</text>
      </svg>
      <figcaption class="donut__caption">By 15 years old 65% of children have seen online pornography. Children were most likely to see it via pop-ups than by searching for it.</figcaption>
    </figure>

    <figure class="donut" style="left:300px; top:310px;">
      <svg width="110" height="110" viewBox="0 0 110 110" role="img" aria-label="53 percent donut chart">
        <circle cx="55" cy="55" r="40" fill="none" stroke="var(--ring)" stroke-width="18"/>
        <circle cx="55" cy="55" r="40" fill="none" stroke="var(--navy)" stroke-width="18" stroke-dasharray="133.2 251.3" transform="rotate(-90 55 55)"/>
        <text x="55" y="60" text-anchor="middle" class="donut__label">53%</text>
      </svg>
      <figcaption class="donut__caption">Just over half of boys (53%) who had seen pornography thought it was 'realistic'.</figcaption>
    </figure>

    <figure class="bars" style="left:30px; top:545px;">
      <div class="bars__chart" role="img" aria-label="Bar chart: parents 33 percent, child 27 percent">
        <div class="bar bar--parents"><span class="bar__value">33%</span><span class="bar__fill">Parents</span></div>
        <div class="bar bar--child"><span class="bar__value">27%</span><span class="bar__fill">Child</span></div>
      </div>
      <figcaption class="bars__caption">One in three parents (33%) claims to filter their child's internet use and one in four (27%) uses monitoring software.</figcaption>
    </figure>

    <figure class="bars" style="left:300px; top:515px;">
      <div class="bars__chart" role="img" aria-label="Bar chart: child 27 percent, parents 33 percent">
        <div class="bar bar--child"><span class="bar__value">27%</span><span class="bar__fill">Child</span></div>
        <div class="bar bar--parents"><span class="bar__value">33%</span><span class="bar__fill">Parents</span></div>
      </div>
      <figcaption class="bars__caption">Overall, only a quarter of children (27%) and a third of parents think parents are effective in helping to keep children safe online.</figcaption>
    </figure>

    <div class="stats__foot"></div>
  </section>

</div>
</body>
</html>
```